Velvet Fern Tagline: Beauty & Balance

I’m looking to create a professional website for my body sculpting, facial, waxing, and wellness spa. I’d like clarity on all required components and integrations needed for a fully functional, client‑friendly platform.**

The website should include:

- **Home Page**
- **About Page**
- **Contact Page**
- **Services Page** (with detailed service descriptions)
- **Meet the Team Page**
- **Product Page** (with e‑commerce capabilities)
- **Blog Section** (multiple posts/pages)
**** Education-
- **Refund & Cancellation Policies Page, Legal Polices ( to discuss potient risk when using products and equipment for services rendered *

**Functionality Requirements: **

- Seamless **integration with external platforms** used for scheduling, client management, or marketing.
- Full **e‑commerce capability**, including:
- “Buy Now” Pay Later” solutions like Pay-Lattice, Vorsta, Quillow and Integration with **Tindle Payments** and similar financing providers
- Ability to manage and sell both **services and retail products**.
- A user‑friendly backend for updating content, products, and blog posts.

Technical Requirements
• HIPAA Compliance: Use platforms like Mavrelo or ClinivaHub to ensure client health data and photos are stored securely. HIPAA Notice: Since you offer post-op services, include a small disclaimer below your contact form: "Please do not share sensitive medical information through this form. Private health details will be collected during your secure, HIPAA-compliant intake process".

• Mobile Optimization: Ensure the site is "responsive" so it looks perfect on smartphones where most clients will book.
• SEO: Include local keywords like "Sacramento Body Sculpting" and "Best Waxing in 95731" to help people find you.

I’m seeking guidance on what is required to build this site effectively, including platform recommendations, integrations, and any technical considerations.

Velvet Fern
Tagline : Beauty and Balance

Logo- I created this logo attached. I want this concept but want it revised properly and I am willing to pay for a revised logo which will not be too far off from what you currently see.

Beauty, Cosmetic, Spa, Wellness, Holistic

```html
<!DOCTYPE html>
<html lang="en">
<head>
<meta charset="utf-8">
<title>Velvet Fern – Our Services</title>
<link href="https://fonts.googleapis.com/css2?family=Libre+Baskerville:wght@400;700&family=Montserrat:wght@400;500;600&display=swap" rel="stylesheet">
<style>
:root{
  --magenta:#c8307f;
  --magenta-dark:#a3206a;
  --plum:#5a2147;
  --ink:#333;
  --muted:#666;
  --rule:#d9d9d9;
  --teal:#1f9e8c;
  --footer-pink:#f6d7e6;
  --white:#fff;
}
*{box-sizing:border-box;margin:0;padding:0}
html,body{width:814px;height:1200px;overflow:hidden;background:var(--white)}
body{font-family:'Montserrat',sans-serif;color:var(--ink);position:relative}
.site-header{height:110px;position:relative}
.brand{position:absolute;left:110px;top:14px;display:flex;align-items:center;gap:8px}
.brand-dot{width:34px;height:34px;border-radius:50%;background:var(--magenta)}
.brand-name{font-family:'Libre Baskerville',serif;font-size:15px;font-weight:700;color:var(--magenta);letter-spacing:.5px}
.topline{position:absolute;right:80px;top:12px;display:flex;gap:14px;align-items:center;font-size:9px;color:var(--muted)}
.topline .item{display:flex;align-items:center;gap:4px}
.social{display:flex;gap:6px}
.social span{width:9px;height:9px;border-radius:50%;background:var(--magenta)}
.main-nav{position:absolute;right:58px;top:62px;display:flex;gap:14px;font-size:9.5px;font-weight:500;color:#444}
.main-nav .active{color:var(--magenta);border-bottom:2px solid var(--magenta);padding-bottom:3px}
.promo-bar{height:40px;background:var(--magenta);display:flex;justify-content:space-around;align-items:center;font-size:9px;color:var(--white);padding:0 80px}
.hero{height:255px;position:relative;background:linear-gradient(90deg,#5d2a52,#7a3466 45%,#4a1c3f);display:flex;align-items:center;justify-content:center}
.hero h1{font-family:'Libre Baskerville',serif;font-weight:400;font-size:36px;color:var(--white)}
.services{position:relative;height:530px}
.services h2{font-family:'Libre Baskerville',serif;font-weight:700;font-size:19px;color:var(--plum);text-align:center;padding-top:48px}
.services h2::after{content:"";display:block;width:50px;height:2px;background:var(--magenta);margin:10px auto 0}
.service-photo{position:absolute;left:122px;top:88px;width:282px;height:350px;background:linear-gradient(160deg,#e7e2dc,#c9b6a8 55%,#8b7466);box-shadow:0 6px 14px rgba(0,0,0,.2)}
.accordion{position:absolute;left:410px;top:88px;width:290px}
.acc-item{display:flex;justify-content:space-between;align-items:center;font-family:'Libre Baskerville',serif;font-size:10.5px;font-weight:700;color:#333;padding:10px 4px;border-bottom:1px solid var(--rule)}
.acc-body{font-family:'Libre Baskerville',serif;font-size:10px;line-height:1.55;color:#444;padding:10px 4px 12px;border-bottom:1px solid var(--rule)}
.btn-pay{position:absolute;left:410px;top:415px;background:var(--magenta);color:var(--white);font-family:'Libre Baskerville',serif;font-weight:700;font-size:12px;padding:10px 14px;border-radius:3px}
.site-footer{position:absolute;top:935px;left:0;width:814px;height:230px;background:linear-gradient(110deg,#fbe3ee,#f3c6dc 50%,#cfe8ef)}
.footer-brand{position:absolute;left:122px;top:28px;display:flex;align-items:center;gap:8px}
.footer-about{position:absolute;left:122px;top:108px;width:140px;font-size:8.5px;line-height:1.55;color:#444}
.footer-links{position:absolute;left:300px;top:108px;list-style:none;font-size:8.5px;line-height:1.5;color:#444}
.footer-contact{position:absolute;left:412px;top:100px;font-size:8.5px;color:#444}
.footer-contact h4{font-size:9px;color:var(--magenta);font-weight:600;margin-bottom:8px}
.footer-contact p{display:flex;align-items:center;gap:6px;margin-bottom:6px}
.footer-contact i{width:10px;height:10px;border-radius:50%;background:var(--teal);display:inline-block}
.bottom-bar{position:absolute;top:1165px;left:0;width:814px;height:35px;background:var(--teal);display:flex;justify-content:space-between;align-items:center;padding:0 110px;font-size:8px;color:var(--white)}
.bottom-bar .social span{background:var(--white)}
</style>
</head>
<body>
<header class="site-header">
  <div class="brand"><span class="brand-dot"></span><span class="brand-name">VELVET FERN</span></div>
  <div class="topline">
    <span class="item"><svg width="9" height="9" viewBox="0 0 10 10"><path d="M2 1l2 2-1 1.5a6 6 0 0 0 2.5 2.5L7 6l2 2-1.5 1.5C4 9 1 6 .5 2.5z" fill="#c8307f"/></svg>+1 916 555 0142</span>
    <span class="item"><svg width="10" height="8" viewBox="0 0 10 8"><rect x=".5" y=".5" width="9" height="7" fill="none" stroke="#c8307f"/><path d="M.5 .5l4.5 4 4.5-4" fill="none" stroke="#c8307f"/></svg>hello@velvetfernspa.com</span>
    <span class="item">www.velvetfernspa.com</span>
    <span class="social"><span></span><span></span><span></span><span></span></span>
  </div>
  <nav class="main-nav">
    <span>HOME</span><span>ABOUT</span><span class="active">SERVICES ▾</span><span>MEET THE TEAM</span><span>PRODUCT ▾</span><span>BLOG ▾</span><span>EDUCATION ▾</span><span>CONTACT</span>
  </nav>
</header>
<div class="promo-bar"><span>Free shipping on orders over $200</span><span>Buy now, pay later on every order</span><span>24/7 Support</span></div>
<section class="hero" role="img" aria-label="Spa therapist applying a facial treatment, purple tinted photo"><h1>Our Services</h1></section>
<section class="services">
  <h2>Our Services</h2>
  <div class="service-photo" role="img" aria-label="Therapist giving a client a facial treatment in a bright treatment room"></div>
  <div class="accordion">
    <div class="acc-item"><span>Lorem Ipsum is simply dummy text</span><span>⌄</span></div>
    <div class="acc-item"><span>Lorem Ipsum is simply dummy text</span><span>⌃</span></div>
    <div class="acc-body">Lorem Ipsum is simply dummy text of the printing and typesetting industry. Lorem Ipsum has been the industry's standard dummy text ever since the 1500s, when an unknown printer took a galley of type and scrambled it to make a type specimen book.</div>
    <div class="acc-item"><span>Lorem Ipsum is simply dummy text</span><span>⌄</span></div>
    <div class="acc-item"><span>Lorem Ipsum is simply dummy text</span><span>⌄</span></div>
    <div class="acc-item"><span>Lorem Ipsum is simply dummy text</span><span>⌄</span></div>
  </div>
  <div class="btn-pay">Tindle Payments</div>
</section>
<footer class="site-footer" role="img" aria-label="Soft pink and teal background with butterflies">
  <div class="footer-brand"><span class="brand-dot"></span><span class="brand-name">VELVET FERN</span></div>
  <p class="footer-about">Lorem Ipsum is simply dummy text of the printing and typesetting industry. Lorem Ipsum has been the best.</p>
  <ul class="footer-links"><li>HOME</li><li>ABOUT</li><li>SERVICES</li><li>MEET THE TEAM</li><li>PRODUCT</li><li>BLOG</li><li>EDUCATION</li><li>CONTACT</li></ul>
  <div class="footer-contact">
    <h4>CONTACT US</h4>
    <p><i></i>+1 916 555 0142</p>
    <p><i></i>+1 916 555 0187</p>
    <p><i></i>hello@velvetfernspa.com</p>
    <p><i></i>www.velvetfernspa.com</p>
  </div>
</footer>
<div class="bottom-bar"><span>Velvet Fern · All rights reserved</span><span class="social"><span></span><span></span><span></span><span></span></span></div>
</body>
</html>
```